One business card required with 2 company logos and 2 people's details

One business card required.
No preference on design - One side could show the 2 different business logos for the companies we own. The reverse could have the details shown below.
Another option could be one business one side and one business on the reverse. Happy to receive designs.

Karen Wibberley
07700 913 258
Joanna Pettifer
07700 927 341

website: truelymarvellous.example
email: info@truelymarvellous.example

website: ironheronoccasions.example
email: info:ironheronoccasions.example

May be nice to have icons instead of the words email/website?

I have included different versions of the logos to help with your design.

Contact Information for Business Card

see project overview

Requirements
Must have
• both company logos, both contact names and contact details

```html
<!DOCTYPE html>
<html lang="en">
<head>
<meta charset="utf-8">
<title>Business Card – Truely Marvellous &amp; Iron Heron Occasions</title>
<link href="https://fonts.googleapis.com/css2?family=Barlow:wght@400;500&family=Pinyon+Script&display=swap" rel="stylesheet">
<style>
  :root {
    --backdrop: #8c8c8c;
    --card: #ffffff;
    --ink: #1c1c1c;
    --ink-soft: #2a2a2a;
    --sky: #4fb3e0;
    --royal: #3f6fc0;
    --navy: #3a3556;
  }
  * { margin: 0; padding: 0; box-sizing: border-box; }
  html, body {
    width: 1200px; height: 1200px; overflow: hidden;
    background: var(--backdrop);
  }
  .card {
    position: absolute; left: 208px; width: 784px; height: 446px;
    background: var(--card);
  }
  .card--contacts { top: 114px; }
  .card--brands { top: 640px; }

  .person-name {
    position: absolute; top: 48px;
    font-family: "Pinyon Script", cursive;
    font-size: 48px; line-height: 1; color: var(--ink);
    white-space: nowrap;
  }
  .person-name--left { left: 53px; }
  .person-name--right { right: 48px; }

  .phone {
    position: absolute; top: 246px;
    display: flex; align-items: center; gap: 12px;
    font-family: "Barlow", sans-serif; font-weight: 500;
    font-size: 26px; line-height: 1; color: var(--ink);
  }
  .phone--left { left: 53px; }
  .phone--right { right: 53px; }
  .phone-icon { width: 16px; height: 26px; }

  .divider {
    position: absolute; left: 53px; top: 308px; width: 677px; height: 1.5px;
    background: linear-gradient(90deg, var(--sky), var(--royal));
  }

  .contact-block {
    position: absolute; top: 340px;
    display: flex; align-items: center; gap: 12px;
    font-family: "Barlow", sans-serif; font-weight: 400;
    font-size: 19px; line-height: 27px; color: var(--ink-soft);
  }
  .contact-block--email { left: 53px; }
  .contact-block--web { right: 54px; text-align: right; }
  .contact-icon { width: 39px; height: 40px; flex: none; }

  .brand {
    position: absolute; top: 92px; transform: translateX(-50%);
    display: flex; flex-direction: column; align-items: center; gap: 26px;
  }
  .brand--marvellous { left: 256px; }
  .brand--heron { left: 548px; }
  .brand-circle {
    width: 170px; height: 170px; border-radius: 50%;
    border: 3px solid currentColor;
  }
  .brand-name {
    font-family: "Barlow", sans-serif; font-weight: 500;
    font-size: 31px; line-height: 1; white-space: nowrap;
  }
  .brand--marvellous { color: var(--navy); }
  .brand--heron { color: var(--royal); }
</style>
</head>
<body>

<section class="card card--contacts">
  <p class="person-name person-name--left">Karen Wibberley</p>
  <p class="person-name person-name--right">Joanna Pettifer</p>

  <p class="phone phone--left">
    <svg class="phone-icon" viewBox="0 0 16 26" aria-hidden="true"><rect x="1" y="1" width="14" height="24" rx="2" fill="none" stroke="var(--sky)" stroke-width="1.3"/><line x1="6" y1="3.5" x2="10" y2="3.5" stroke="var(--sky)" stroke-width="1"/><line x1="6.5" y1="22.5" x2="9.5" y2="22.5" stroke="var(--sky)" stroke-width="1"/></svg>
    <span>07700 913 258</span>
  </p>
  <p class="phone phone--right">
    <span>07700 927 341</span>
    <svg class="phone-icon" viewBox="0 0 16 26" aria-hidden="true"><rect x="1" y="1" width="14" height="24" rx="2" fill="none" stroke="var(--sky)" stroke-width="1.3"/><line x1="6" y1="3.5" x2="10" y2="3.5" stroke="var(--sky)" stroke-width="1"/><line x1="6.5" y1="22.5" x2="9.5" y2="22.5" stroke="var(--sky)" stroke-width="1"/></svg>
  </p>

  <div class="divider"></div>

  <div class="contact-block contact-block--email">
    <svg class="contact-icon" viewBox="0 0 40 40" aria-hidden="true">
      <path d="M2 16 L20 2 L38 16 L38 38 L2 38 Z" fill="var(--royal)"/>
      <rect x="7" y="14" width="26" height="12" fill="#fff"/>
      <path d="M2 16 L20 28 L38 16" fill="none" stroke="#fff" stroke-width="2.5"/>
      <path d="M2 38 L16 26 M38 38 L24 26" stroke="#fff" stroke-width="2.5"/>
      <path d="M7 14 L20 23 L33 14 Z" fill="var(--royal)"/>
    </svg>
    <div>
      <div>info@truelymarvellous.example</div>
      <div>info@ironheronoccasions.example</div>
    </div>
  </div>

  <div class="contact-block contact-block--web">
    <div>
      <div>truelymarvellous.example</div>
      <div>ironheronoccasions.example</div>
    </div>
    <svg class="contact-icon" viewBox="0 0 40 40" aria-hidden="true" fill="none" stroke="var(--royal)" stroke-width="2">
      <circle cx="20" cy="20" r="18"/>
      <ellipse cx="20" cy="20" rx="8" ry="18"/>
      <line x1="20" y1="2" x2="20" y2="38"/>
      <line x1="2" y1="20" x2="38" y2="20"/>
      <path d="M5 11 H35 M5 29 H35"/>
    </svg>
  </div>
</section>

<section class="card card--brands">
  <div class="brand brand--marvellous">
    <span class="brand-circle" aria-hidden="true"></span>
    <p class="brand-name">Truely Marvellous</p>
  </div>
  <div class="brand brand--heron">
    <span class="brand-circle" aria-hidden="true"></span>
    <p class="brand-name">Iron Heron Occasions</p>
  </div>
</section>

</body>
</html>
```